Bref créative
Brisk Mug Co
Stationary pack - card, compliment slip, headed paper.
Bright & Fun-filled
Tom Reeve
Managing Director
14 Fenwick Rd
Kelbridge
Morvale
Northland
KA7 2QP
tbc
tom@briskmugco.com
www.briskmugco.com
This is our logo. We would obviously like something to tie inn with this.

```html
<!DOCTYPE html>
<html lang="en">
<head>
<meta charset="utf-8">
<title>Brisk Mug Co – Stationery Pack</title>
<link rel="stylesheet" href="https://fonts.googleapis.com/css2?family=Arimo:wght@400;700&display=swap">
<style>
  :root {
    --brand-blue: #1a76c6;
    --brand-blue-deep: #1565b0;
    --brand-orange: #f6a421;
    --paper: #ffffff;
    --board: #ffffff;
    --board-edge: #d9d9d9;
    --page-bg: #f4f4f4;
    --text-blue: #1a76c6;
  }
  * { box-sizing: border-box; margin: 0; padding: 0; }
  html, body { width: 1200px; height: 921px; overflow: hidden; background: var(--page-bg); }
  body { font-family: "Arimo", Arial, sans-serif; position: relative; }

  .board {
    position: absolute; left: 42px; top: 42px; width: 1116px; height: 838px;
    background: var(--board); border: 2px solid var(--board-edge);
  }
  .sheet {
    position: absolute; background: var(--paper);
    border: 1px solid #e2e2e2;
    box-shadow: 4px 5px 10px rgba(0,0,0,0.18);
    overflow: hidden;
  }
  .sheet .band { position: absolute; left: 0; top: 0; width: 100%; display: block; }

  .wordmark {
    font-weight: 700; color: var(--brand-blue); letter-spacing: 0.5px;
    display: inline-flex; align-items: center; gap: 6px; white-space: nowrap;
  }
  .wordmark .dot { display: inline-block; border-radius: 50%; background: var(--brand-orange); }

  /* Headed paper */
  .headed-paper { left: 366px; top: 26px; width: 597px; height: 775px; }
  .headed-paper .wordmark { position: absolute; top: 110px; left: 0; width: 100%; justify-content: center; font-size: 22px; }
  .headed-paper .wordmark .dot { width: 10px; height: 10px; }
  .headed-paper .footer-address {
    position: absolute; bottom: 30px; width: 100%; text-align: center;
    font-size: 10px; font-weight: 700; color: var(--text-blue);
  }

  /* Compliment slip */
  .compliment-slip { left: 26px; top: 276px; width: 675px; height: 292px; }
  .compliment-slip .wordmark { position: absolute; left: 48px; top: 118px; font-size: 18px; }
  .compliment-slip .wordmark .dot { width: 8px; height: 8px; }
  .compliment-slip .address {
    position: absolute; left: 48px; top: 148px; font-size: 9px; line-height: 12px;
    font-weight: 700; color: var(--text-blue); text-align: center;
  }

  /* Business card front */
  .card-front { left: 831px; top: 276px; width: 250px; height: 148px; }
  .card-front .wordmark { position: absolute; top: 58px; width: 100%; justify-content: center; font-size: 12px; gap: 4px; }
  .card-front .wordmark .dot { width: 6px; height: 6px; }
  .card-front .contact {
    position: absolute; top: 84px; width: 100%; text-align: center; color: var(--text-blue);
    font-size: 6px; line-height: 8px;
  }
  .card-front .contact .name { font-size: 9px; font-weight: 700; line-height: 11px; }
  .card-front .contact .role { margin-bottom: 5px; }

  /* Business card back */
  .card-back { left: 831px; top: 468px; width: 250px; height: 143px; background: var(--brand-blue); border-color: var(--brand-blue-deep); }
  .card-back .wordmark-faint {
    position: absolute; left: 0; top: 48px; width: 100%; text-align: center;
    font-weight: 700; font-size: 24px; color: rgba(255,255,255,0.35); letter-spacing: 1px;
  }
  .card-back .web {
    position: absolute; left: 80px; bottom: 30px; font-size: 6px; font-weight: 700; color: #ffffff;
  }
</style>
</head>
<body>
  <main class="board">

    <section class="sheet headed-paper" aria-label="Headed paper">
      <svg class="band" width="597" height="72" viewBox="0 0 597 72" aria-hidden="true">
        <path d="M0 0 H597 V58 Q298 16 0 58 Z" fill="var(--brand-blue)"/>
        <path d="M0 65 Q298 23 597 65" fill="none" stroke="var(--brand-orange)" stroke-width="6"/>
      </svg>
      <div class="wordmark"><span class="dot"></span>Brisk Mug Co</div>
      <p class="footer-address">14 Fenwick Rd, Kelbridge, Morvale, Northland KA7 2QP</p>
    </section>

    <section class="sheet compliment-slip" aria-label="Compliment slip">
      <svg class="band" width="675" height="62" viewBox="0 0 675 62" aria-hidden="true">
        <path d="M0 0 H675 V48 Q337 8 0 48 Z" fill="var(--brand-blue)"/>
        <path d="M0 55 Q337 15 675 55" fill="none" stroke="var(--brand-orange)" stroke-width="5"/>
      </svg>
      <div class="wordmark"><span class="dot"></span>Brisk Mug Co</div>
      <p class="address">14 Fenwick Rd, Kelbridge, Morvale<br>Northland KA7 2QP</p>
    </section>

    <section class="sheet card-front" aria-label="Business card front">
      <svg class="band" width="250" height="36" viewBox="0 0 250 36" aria-hidden="true">
        <path d="M0 0 H250 V28 Q125 10 0 28 Z" fill="var(--brand-blue)"/>
        <path d="M0 32 Q125 14 250 32" fill="none" stroke="var(--brand-orange)" stroke-width="3"/>
      </svg>
      <div class="wordmark"><span class="dot"></span>Brisk Mug Co</div>
      <div class="contact">
        <p class="name">Tom Reeve</p>
        <p class="role">Managing Director</p>
        <p>14 Fenwick Rd, Kelbridge, Morvale, Northland KA7 2QP</p>
        <p>Tel: tbc · Email: tom@briskmugco.com</p>
      </div>
    </section>

    <section class="sheet card-back" aria-label="Business card back">
      <p class="wordmark-faint">Brisk Mug Co</p>
      <p class="web">www.briskmugco.com</p>
    </section>

  </main>
</body>
</html>
```